Qarnetix EIRL Business Card Design Project

We need a business card design for a New Business Intelligence Consultant. We bring a complete service to the client from first consulting meeting to help desk and system improvement.

I will upload the company logo and I like to use the logo colors on the card. Feel free to use all logo components on the design, for example one side with the black logo using complete card and the other side only the red shape (is an example, feel absolutely free :)).

The principal idea is to sell a professional service and a modern company.

Target Market(s)

IT Business Intelligence Clients

Industry/Entity Type

Professional Service

Requirements
Nice to have
• - Use the logo colors and minimize white sections.
- Rounded borders
Should not have
• I don't want to see any references to people working on a meeting or office photos or any computers related logos.

```html
<!DOCTYPE html>
<html lang="en">
<head>
<meta charset="utf-8">
<title>Qarnetix EIRL — Business Card</title>
<link rel="stylesheet" href="https://fonts.googleapis.com/css2?family=Michroma&family=Ubuntu:wght@400;500&display=swap">
<style>
  :root{
    --page:#f0f0f0;
    --card-dark:#2e2e30;
    --card-mid:#474749;
    --red:#e30613;
    --grey-light:#b0b0b2;
    --grey-mid:#6a6a6c;
    --white:#ffffff;
  }
  *{margin:0;padding:0;box-sizing:border-box}
  html,body{width:1200px;height:960px;overflow:hidden;background:var(--page)}
  .canvas{position:relative;width:1200px;height:960px}
  .card{
    position:absolute;left:220px;width:760px;height:430px;border-radius:18px;overflow:hidden;
    background:var(--card-dark);box-shadow:0 10px 30px rgba(0,0,0,.35);
  }
  .card--front{top:30px}
  .card--back{top:500px}
  .card__texture{
    position:absolute;inset:0;
    background:radial-gradient(ellipse at 50% 40%,var(--card-mid) 0%,var(--card-dark) 75%);
  }
  .brand{
    position:absolute;left:48px;top:42px;display:flex;align-items:center;gap:16px;
    font-family:"Ubuntu",sans-serif;font-weight:500;font-size:58px;color:var(--red);line-height:1;
  }
  .brand__mark{width:48px;height:48px;background:var(--grey-light);border-radius:4px}
  .person{position:absolute;left:40px;top:160px;width:360px}
  .person__name{
    font-family:"Michroma",sans-serif;font-size:24px;color:var(--white);letter-spacing:2px;
    padding:0 0 6px 40px;border-bottom:3px solid var(--red);
  }
  .person__role{
    font-family:"Michroma",sans-serif;font-size:13px;color:var(--white);letter-spacing:2px;
    text-align:right;padding:6px 20px 0 0;
  }
  .contact{position:absolute;left:56px;top:262px;list-style:none;
    font-family:"Michroma",sans-serif;font-size:13px;color:var(--white);letter-spacing:1px}
  .contact li{display:flex;align-items:center;gap:30px;margin-bottom:16px}
  .contact svg{width:16px;height:16px;flex:none}
  .address{position:absolute;left:48px;bottom:40px;
    font-family:"Michroma",sans-serif;font-size:10px;line-height:1.35;color:var(--white);letter-spacing:1px}
  .feature-block{position:absolute;right:60px;top:110px;width:230px;height:230px;border-radius:6px;
    background:var(--grey-mid)}
  .feature-block::after{content:"";position:absolute;right:0;top:0;width:50px;height:100%;background:var(--red);border-radius:0 6px 6px 0}
  .back__band{position:absolute;left:30px;top:230px;width:22px;height:170px;background:var(--red)}
  .back__sign{position:absolute;right:44px;bottom:44px;display:flex;flex-direction:column;align-items:flex-end;gap:18px}
  .back__mark{width:60px;height:60px;background:var(--grey-light);border-radius:4px}
  .back__url{font-family:"Ubuntu",sans-serif;font-size:28px;color:var(--white)}
</style>
</head>
<body>
<main class="canvas">
  <section class="card card--front" aria-label="Card front">
    <div class="card__texture" role="img" aria-label="Dark graphite texture with fine repeating dot pattern"></div>
    <div class="brand"><span class="brand__mark"></span>qarnetix</div>
    <div class="person">
      <div class="person__name">NAME SURNAME</div>
      <div class="person__role">POSITION</div>
    </div>
    <ul class="contact">
      <li>
        <svg viewBox="0 0 16 16" fill="none" stroke="#fff" stroke-width="1.5"><path d="M4 1.5l2 3-1.5 1.5a8 8 0 0 0 5.5 5.5L11.5 10l3 2-1.5 2.5C7 14 2 9 1.5 3z"/></svg>
        <span>+11 555-010-234</span>
      </li>
      <li>
        <svg viewBox="0 0 16 16" fill="none" stroke="#fff" stroke-width="1.5"><rect x="1.5" y="3.5" width="13" height="9"/><path d="M1.5 3.5l6.5 5 6.5-5"/></svg>
        <span>OFFICE@QARNETIX.COM</span>
      </li>
    </ul>
    <address class="address" style="font-style:normal">QARNETIX<br>STREET ADRESS<br>12-345 CITY<br>COUNTRY</address>
    <div class="feature-block"></div>
  </section>

  <section class="card card--back" aria-label="Card back">
    <div class="card__texture" role="img" aria-label="Dark graphite texture with fine repeating dot pattern"></div>
    <div class="back__band"></div>
    <div class="back__sign">
      <span class="back__mark"></span>
      <span class="back__url">www.qarnetix.com</span>
    </div>
  </section>
</main>
</body>
</html>
```